Capability Statement
Small Business Marketing Sheet
Creative Brief
Harbor Lantern, LLC Bold Vision, Lasting Growth
We want a front and back document that lists all the information provided below in addition to our company logo. We would like this capability statement to stand out from our peers in the market and be something highly professional.
The following information must be within the document:
Corporate Summary
Harbor Lantern, LLC is a Veteran owned Small Business specializing in management and executive management consulting. The founders of this firm have a combined 60 years’ experience in military, government service, federal and state and local consulting within the Department of Defense, Intelligence Community, government agencies, and state entities.
Integrity, collaboration, innovation, and integration with our clients and partners are the cornerstones of Harbor Lantern, LLC mission success. Harbor Lantern, LLC will achieve client and partner satisfaction by providing the highest quality products, services, and analyses coupled with the right personnel and with unwavering ethical standards.
Solutions
Harbor Lantern. LLC has the skill set, experience, and expertise to provide and foster maximum client and partner satisfaction in the following solutions:
o Federal, State, and Local Policy Development and Analysis
o Planning, Programming, Budgeting, and Execution (PPBE)
o Performance Measure Development and Implementation
o Program Management, Change Management and Strategic Planning
o Logistic and Inventory Management
Key Personnel
President
Tom vanOstrel is a highly skilled, knowledgeable, accomplished project management professional with over 20 years’ experience leading both federal, military and private industry sectors. Mr. vanOstrel is an 8 year veteran of the Air Force and holds a Master of Science and Bachelor of Science in Mechanical Engineering. Mr. vanOstrel is certified as a Project Management Professional (PMP) and Certified Defense Financial Manager (CDFM) by the Venture Planning Guild and National Circle of Defense Bursars, respectively.
Vice President
Gordon Whitfield has served as a senior manager both inside the Federal Government and in private industry. He is an expert in Planning, Programming, Budgeting and Execution (PPBE), Program Management, Policy Development, and Customer Focused Performance Metrics. Mr. Whitfield is a 24 year veteran in both the US Navy and Army respectively. He holds a Master of Business Administration, a Master of Public Administration, and a Master of Science in Contract and Acquisition Management.
Managing Director
Steven Collard has served as a senior analyst in multiple firms doing business with the Federal Government. He is an expert in Federal human resource systems and processes as well as major Federal acquisition systems. Mr. Collard is a 12 year US Army veteran and holds a Bachelor of Science in Business. He is a Certified Defense Financial Manager (CDFM) by the National Circle of Defense Bursars.
NAICS Codes – 541611, 541612, 541613, 541614, 541618, 541620, 561110
CAGE Code: 9QRT4
DUNS: 093157608
Business Classification: Small, VOSB
Contact Us: info@h-lant.example
Location: 51932 Wrenfield Court Leesburg, VA 20176
Fax: 703-555-0182
Office: 703-555-0147
Consulting
Large Businesses, Small Businesses, Federal Government, State & Local Government
This will be used to attract key market peers and develop business relationships so it needs to stand out, while also being professional in appearance. Must provide all the information within the details section in a front and back two page total design.
Pictures are encouraged.
Must contain all the information provided within the details section. Will need to contain our company logo.

```html
<!DOCTYPE html>
<html lang="en">
<head>
<meta charset="utf-8">
<title>Harbor Lantern, LLC — Capability Statement</title>
<link href="https://fonts.googleapis.com/css2?family=Cinzel:wght@600&family=Open+Sans:ital,wght@0,400;0,600;0,700;1,400&family=Lora:ital,wght@1,600&display=swap" rel="stylesheet">
<style>
  :root {
    --navy: #123a6b;
    --blue: #1f5fa3;
    --sky: #4b8fd0;
    --pale: #e8eef6;
    --red: #c4242b;
    --ink: #2f3440;
    --muted: #6b7280;
    --paper: #ffffff;
    --backdrop: #dcdfe4;
  }
  * { box-sizing: border-box; margin: 0; padding: 0; }
  html, body { width: 1200px; height: 770px; overflow: hidden; }
  body { background: var(--backdrop); font-family: "Open Sans", Arial, sans-serif; color: var(--ink); position: relative; }

  .sheet { position: absolute; top: 60px; width: 500px; height: 650px; background: var(--paper); box-shadow: 0 6px 18px rgba(0,0,0,.25); overflow: hidden; }
  .sheet--front { left: 70px; display: flex; flex-direction: column; }
  .sheet--back { left: 630px; }

  .brand { display: flex; align-items: center; gap: 8px; }
  .brand__dot { width: 22px; height: 22px; border-radius: 50%; background: var(--red); }
  .brand__name { font-family: "Cinzel", Georgia, serif; font-weight: 600; color: var(--navy); font-size: 20px; letter-spacing: 1px; }

  /* front */
  .masthead { flex: 0 0 76px; display: flex; justify-content: center; align-items: center; border-bottom: 3px solid var(--blue); }
  .hero { flex: 0 0 96px; background: linear-gradient(180deg, var(--blue), var(--navy)); display: flex; padding: 16px 22px; gap: 20px; color: #fff; }
  .hero__title { font-family: "Lora", Georgia, serif; font-style: italic; font-weight: 600; font-size: 19px; line-height: 1.2; width: 180px; }
  .hero__text { font-size: 8px; line-height: 1.55; flex: 1; color: #dfe9f5; }
  .visuals { flex: 0 0 78px; display: flex; }
  .visual--puzzle { width: 200px; background: radial-gradient(circle at 50% 50%, #d8343a, #f2f2f2 70%); }
  .visual--team { flex: 1; background: linear-gradient(135deg, #9fb6cf, #4c6a8d); }

  .section-title { display: inline-block; background: var(--navy); color: #fff; font-size: 10px; font-weight: 700; text-transform: uppercase; letter-spacing: .5px; padding: 3px 10px; border-left: 4px solid var(--red); }
  .summary { flex: 0 0 174px; display: flex; padding: 12px 18px 0; gap: 14px; }
  .summary__body { flex: 1; }
  .summary__body p { font-size: 7.4px; line-height: 1.5; margin-top: 5px; }
  .visual--meeting { width: 130px; height: 110px; background: linear-gradient(160deg, #c9d3de, #6f8196); border: 3px solid var(--pale); }

  .goals { flex: 0 0 40px; display: flex; }
  .goals__tag { width: 110px; background: var(--red); color: #fff; font-size: 7.5px; font-weight: 700; padding: 7px 10px; line-height: 1.35; }
  .goals__band { flex: 1; background: var(--navy); color: #fff; font-size: 7.5px; font-weight: 600; padding: 8px 12px; line-height: 1.45; }

  .solutions { flex: 1; display: flex; padding: 10px 18px; gap: 14px; background: var(--pale); }
  .visual--office { flex: 0 0 120px; height: 110px; background: linear-gradient(150deg, #b9c7d6, #5a7494); }
  .solutions__body p { font-size: 7.4px; line-height: 1.5; margin-top: 5px; }
  .solutions__list { list-style: none; margin-top: 4px; }
  .solutions__list li { font-size: 7.4px; line-height: 1.55; padding-left: 9px; position: relative; }
  .solutions__list li::before { content: ""; position: absolute; left: 0; top: 4px; width: 4px; height: 4px; background: var(--red); }

  .footer-bar { flex: 0 0 40px; background: var(--navy); color: #fff; font-size: 10px; font-weight: 600; display: flex; align-items: center; justify-content: flex-end; padding-right: 22px; border-top: 3px solid var(--red); }

  /* back */
  .personnel { padding: 26px 28px 0; }
  .personnel__heading { font-size: 12px; font-weight: 700; color: var(--navy); text-transform: uppercase; letter-spacing: 1px; padding-bottom: 5px; border-bottom: 2px solid var(--pale); }
  .profile { margin-top: 14px; }
  .profile__role { display: inline-block; background: var(--red); color: #fff; font-size: 8.5px; font-weight: 700; padding: 3px 12px; }
  .profile__bar { height: 2px; background: var(--pale); margin-bottom: 6px; }
  .profile p { font-size: 7.6px; line-height: 1.6; }

  .facts { position: absolute; bottom: 0; left: 0; right: 0; height: 150px; background: linear-gradient(180deg, var(--blue), var(--navy)); color: #fff; display: flex; padding: 18px 20px; gap: 14px; border-top: 4px solid var(--red); }
  .facts__col { flex: 1; font-size: 7.2px; line-height: 1.6; }
  .facts__col strong { font-weight: 700; }
  .facts__brand { flex: 0 0 140px; display: flex; align-items: center; justify-content: center; background: var(--paper); border-radius: 3px; height: 60px; align-self: center; }
  .facts__brand .brand__name { font-size: 12px; }
  .facts__brand .brand__dot { width: 14px; height: 14px; }
  .facts__col--right { text-align: right; }
</style>
</head>
<body>

<section class="sheet sheet--front">
  <header class="masthead">
    <div class="brand"><span class="brand__dot"></span><span class="brand__name">Harbor Lantern, LLC</span></div>
  </header>

  <div class="hero">
    <h1 class="hero__title">Bold Vision, Lasting Growth</h1>
    <p class="hero__text">Harbor Lantern, LLC is a management consulting firm focused on helping customers achieve measurable results through disciplined planning, thoughtful analysis, and practical execution across federal, state, and local programs.</p>
  </div>

  <div class="visuals">
    <div class="visual visual--puzzle" role="img" aria-label="Red puzzle piece fitting into white pieces"></div>
    <div class="visual visual--team" role="img" aria-label="Business professionals in discussion"></div>
  </div>

  <div class="summary">
    <div class="summary__body">
      <h2 class="section-title">Corporate Summary</h2>
      <p>Harbor Lantern, LLC is a Veteran owned Small Business specializing in management and executive management consulting. The founders of this firm have a combined 60 years’ experience in military, government service, federal and state and local consulting within the Department of Defense, Intelligence Community, government agencies, and state entities.</p>
      <p>Integrity, collaboration, innovation, and integration with our clients and partners are the cornerstones of Harbor Lantern, LLC mission success. Harbor Lantern, LLC will achieve client and partner satisfaction by providing the highest quality products, services, and analyses coupled with the right personnel and with unwavering ethical standards.</p>
    </div>
    <div class="visual visual--meeting" role="img" aria-label="Consultants meeting around a table"></div>
  </div>

  <div class="goals">
    <div class="goals__tag">What we bring to every partnership</div>
    <div class="goals__band">Our Goals – Performance Based Processes – Integrated Solutions – Client Relationship Management – Education, Experience, and Innovative Solutions</div>
  </div>

  <div class="solutions">
    <div class="visual visual--office" role="img" aria-label="Professional working at a laptop"></div>
    <div class="solutions__body">
      <h2 class="section-title">Solutions</h2>
      <p>Harbor Lantern. LLC has the skill set, experience, and expertise to provide and foster maximum client and partner satisfaction in the following solutions:</p>
      <ul class="solutions__list">
        <li>Federal, State, and Local Policy Development and Analysis</li>
        <li>Planning, Programming, Budgeting, and Execution (PPBE)</li>
        <li>Performance Measure Development and Implementation</li>
        <li>Program Management, Change Management and Strategic Planning</li>
        <li>Logistic and Inventory Management</li>
      </ul>
    </div>
  </div>

  <footer class="footer-bar">www.h-lant.example</footer>
</section>

<section class="sheet sheet--back">
  <div class="personnel">
    <h2 class="personnel__heading">Key Personnel</h2>

    <article class="profile">
      <span class="profile__role">President</span>
      <div class="profile__bar"></div>
      <p>Tom vanOstrel is a highly skilled, knowledgeable, accomplished project management professional with over 20 years’ experience leading both federal, military and private industry sectors. Mr. vanOstrel is an 8 year veteran of the Air Force and holds a Master of Science and Bachelor of Science in Mechanical Engineering. Mr. vanOstrel is certified as a Project Management Professional (PMP) and Certified Defense Financial Manager (CDFM) by the Venture Planning Guild and National Circle of Defense Bursars, respectively.</p>
    </article>

    <article class="profile">
      <span class="profile__role">Vice President</span>
      <div class="profile__bar"></div>
      <p>Gordon Whitfield has served as a senior manager both inside the Federal Government and in private industry. He is an expert in Planning, Programming, Budgeting and Execution (PPBE), Program Management, Policy Development, and Customer Focused Performance Metrics. Mr. Whitfield is a 24 year veteran in both the US Navy and Army respectively. He holds a Master of Business Administration, a Master of Public Administration, and a Master of Science in Contract and Acquisition Management.</p>
    </article>

    <article class="profile">
      <span class="profile__role">Managing Director</span>
      <div class="profile__bar"></div>
      <p>Steven Collard has served as a senior analyst in multiple firms doing business with the Federal Government. He is an expert in Federal human resource systems and processes as well as major Federal acquisition systems. Mr. Collard is a 12 year US Army veteran and holds a Bachelor of Science in Business. He is a Certified Defense Financial Manager (CDFM) by the National Circle of Defense Bursars.</p>
    </article>
  </div>

  <footer class="facts">
    <div class="facts__col">
      <strong>NAICS Codes</strong> – 541611, 541612, 541613, 541614, 541618, 541620, 561110<br>
      <strong>CAGE Code:</strong> 9QRT4<br>
      <strong>DUNS:</strong> 093157608<br>
      <strong>Business Classification:</strong> Small, VOSB<br>
      <strong>Consulting:</strong> Large Businesses, Small Businesses, Federal Government, State &amp; Local Government
    </div>
    <div class="facts__brand">
      <div class="brand"><span class="brand__dot"></span><span class="brand__name">Harbor Lantern</span></div>
    </div>
    <div class="facts__col facts__col--right">
      <strong>Contact Us:</strong> info@h-lant.example<br>
      <strong>Location:</strong> 51932 Wrenfield Court<br>Leesburg, VA 20176<br>
      <strong>Fax:</strong> 703-555-0182<br>
      <strong>Office:</strong> 703-555-0147<br>
      www.h-lant.example
    </div>
  </footer>
</section>

</body>
</html>
```